Design a Consultation and HR Services Website "Shift Pathways"

Consultation and HR Services
I am looking for a design gives the look and feel of Varden Calloway and Ferrovane
we need a high-quality graphics website that looks rich and expensive.
we are working as an affiliate for international consultation firms and sole agent for international HR products.
we are a group of consultants for the Middle East.
we will get the global practices to local practices.

Reason: I am not getting enough options and designs. I am not getting what I was looking for in matter of look and feel. looking for something rich and luxury with black background and rich font. www.blockvault.example www.lucindavarga.example 71dormerplace.example/ www.velquo.example/rd/en/ morvethhouse.example/ www.velquo.example/rd/en/ www.quillen.example/ www.theplaudits.example/ .

Target Market(s)

Corporate all size and industries in GCC

Industry/Entity Type

Management Consulting

Coding

Coded - Design and coding required

Number of Pages Required

5+ page

Font styles to use
Sans Serif
Script

Colors
ffffff
ecf7fb
cee9f5
85cae6
33a6d7
0592cd
000000
848484

Requirements
Must have
• This is the looks and feel that I'm looking for.
• http://www.blockvault.example/?channel=display&subchannel=sitemuse
• http://www.lucindavarga.example/lvny-private/en/
• http://71dormerplace.example/
• http://www.velquo.example/rd/en/
• http://morvethhouse.example/
• http://www.quillen.example/
• http://www.theplaudits.example/
• Home
• Who we are?
• What we do?
• HR & OD Consultation
• Executive Coaching
• Assesment Cemter
• HRIS & Outsourcing
• Testimonials
• Our Partners
• Contact Us
• We need support on Technical righting...

```html
<!DOCTYPE html>
<html lang="en">
<head>
<meta charset="utf-8">
<title>Shift Pathways — Consultation &amp; HR Services</title>
<link rel="stylesheet" href="https://fonts.googleapis.com/css2?family=Dancing+Script:wght@500;600&family=Roboto:ital,wght@0,400;0,500;0,700;1,400&display=swap">
<style>
:root{
  --white:#ffffff;
  --ice:#ecf7fb;
  --mist:#cee9f5;
  --sky:#85cae6;
  --azure:#33a6d7;
  --brand:#0592cd;
  --black:#000000;
  --grey:#848484;
  --ink:#222222;
  --script:"Dancing Script", cursive;
  --sans:"Roboto", Arial, sans-serif;
}
*{box-sizing:border-box;margin:0;padding:0}
html,body{width:1200px;height:3390px;overflow:hidden;background:var(--white);font-family:var(--sans);color:var(--ink)}
.page{position:relative;width:1200px;height:3390px}
.abs{position:absolute}

/* header */
.site-header{left:0;top:0;width:1200px;height:102px;background:var(--white)}
.brand{display:flex;align-items:center;gap:10px;justify-content:center}
.brand-mark{width:22px;height:22px;background:var(--brand)}
.brand-name{font-family:var(--sans);font-weight:500;font-size:24px;color:var(--brand)}
.site-header .brand{position:absolute;left:450px;top:32px;width:300px}
.social{position:absolute;left:1008px;top:42px;display:flex;gap:20px}
.social span{width:16px;height:16px;border-radius:50%;background:#9a9a9a}
.social span:first-child{background:var(--brand)}

/* nav panel */
.nav-panel{left:0;top:0;width:407px;height:606px;background:#050505;z-index:3}
.nav-close{position:absolute;left:72px;top:38px}
.nav-list{position:absolute;left:75px;top:112px;width:270px;list-style:none}
.nav-list li{height:73px;display:flex;align-items:center;border-bottom:1px solid #2a2a2a;color:var(--brand);font-size:21px;letter-spacing:.3px}
.nav-list li:last-child{border-bottom:none}

/* hero */
.hero{left:407px;top:102px;width:793px;height:504px;background:linear-gradient(180deg,#4a4f57 0%,#2f3540 45%,#5a606a 100%)}
.hero-photo{position:absolute;left:0;top:102px;width:1200px;height:504px;background:linear-gradient(180deg,#50555e 0%,#323944 50%,#616772 100%)}
.hero-title{left:0;top:240px;width:1200px;text-align:center;font-family:var(--script);font-size:78px;color:var(--white);z-index:4}
.hero-sub{left:380px;top:350px;width:440px;text-align:center;font-size:20px;line-height:30px;color:var(--white);z-index:4}
.hero-next{left:1100px;top:320px;z-index:4}
.hero-dots{left:565px;top:556px;display:flex;gap:12px;z-index:4}
.hero-dots span{width:11px;height:11px;border-radius:50%;background:var(--white)}
.hero-dots span:first-child{background:var(--azure)}

/* dividers & titles */
.divider{left:75px;width:1050px;height:40px}
.section-title{left:0;width:1200px;text-align:center;font-family:var(--script);font-size:50px;color:var(--black)}

/* services */
.service{width:270px;text-align:center}
.service-icon{width:88px;height:88px;border-radius:50%;margin:0 auto;display:flex;align-items:center;justify-content:center;border:2px solid #9a9a9a;background:linear-gradient(180deg,#ffffff,#e6e6e6)}
.service-icon.is-active{border:3px solid var(--brand);background:var(--white)}
.service h3{margin-top:22px;font-size:23px;font-weight:500;color:var(--ink)}
.service.is-active h3{color:var(--brand)}
.service p{margin-top:12px;font-size:14px;line-height:22px;color:#555}

/* feature rows */
.feature-photo{width:600px;height:404px}
.feature-panel{width:600px;height:404px;background:var(--brand)}
.feature-panel h2{position:absolute;left:67px;top:66px;font-family:var(--script);font-weight:500;font-size:46px;color:var(--white)}
.feature-panel p{position:absolute;left:67px;top:140px;width:470px;font-size:14.5px;line-height:22px;color:var(--white)}
.feature-panel.left h2,.feature-panel.left p{left:75px}
.btn{position:absolute;left:67px;top:283px;width:190px;height:46px;display:flex;align-items:center;justify-content:center;font-size:15px;color:var(--white)}
.feature-panel.left .btn{left:75px}
.btn-solid{background:var(--black)}
.btn-outline{border:2px solid #111}

/* testimonials */
.quote{left:110px;top:2556px;width:980px;text-align:center;font-style:italic;font-size:14.5px;line-height:30px;color:#444}
.slider-arrow{top:2622px}
.avatar{left:560px;top:2660px;width:80px;height:80px;border-radius:50%;background:radial-gradient(circle,#d9d9d9,#9a9a9a);border:3px solid var(--white);box-shadow:0 0 0 1px #ccc}
.quote-mark{left:570px;top:2712px;width:60px;text-align:center;font-family:Georgia,serif;font-size:50px;line-height:50px;color:var(--brand)}

/* footer */
.site-footer{left:0;top:2814px;width:1200px;height:434px;background:var(--black)}
.footer-title{font-family:var(--script);font-weight:500;font-size:46px;color:var(--white)}
.field{background:var(--black);border:1px solid #cfcfcf;color:var(--white);font-size:14px;padding:10px 12px}
.send{left:515px;top:3169px;width:188px;height:46px;background:var(--azure);color:var(--white);font-size:16px;display:flex;align-items:center;justify-content:center}
.contact-name{left:766px;top:2950px;font-size:17px;font-weight:700;color:var(--azure)}
.contact-addr{left:766px;top:2980px;font-size:14px;line-height:24px;color:#9a9a9a}
.contact-list{left:766px;top:3030px;list-style:none}
.contact-list li{display:flex;align-items:center;gap:16px;height:28px;font-size:14px;color:#d8d8d8}
.contact-list li:first-child{color:var(--azure)}

/* bottom bar */
.bottom .brand{position:absolute;left:450px;top:3262px;width:300px}
.copyright{left:0;top:3340px;width:1200px;text-align:center;font-size:12px;color:var(--grey)}
</style>
</head>
<body>
<div class="page">

  <header class="site-header abs">
    <div class="brand"><span class="brand-mark"></span><span class="brand-name">Shift Pathways</span></div>
    <div class="social"><span></span><span></span><span></span><span></span></div>
  </header>

  <div class="hero-photo" role="img" aria-label="Team of business consultants in suits standing together in an office lobby"></div>

  <nav class="nav-panel abs">
    <svg class="nav-close" width="24" height="24" viewBox="0 0 24 24"><path d="M2 2L22 22M22 2L2 22" stroke="#fff" stroke-width="2"/></svg>
    <ul class="nav-list">
      <li>HOME</li>
      <li>WHO WE ARE?</li>
      <li>WHAT WE DO?</li>
      <li>WHO WE SERVE?</li>
      <li>WHOM WE HELP?</li>
      <li>LET US TALK</li>
    </ul>
  </nav>

  <h1 class="hero-title abs">Shift Pathways</h1>
  <p class="hero-sub abs">Aliquam nibh a dui iaculis viverra id a velit egestas risus in magna varius commodo.</p>
  <svg class="hero-next abs" width="26" height="60" viewBox="0 0 26 60"><path d="M4 4L22 30L4 56" fill="none" stroke="#fff" stroke-opacity=".7" stroke-width="2"/></svg>
  <div class="hero-dots abs"><span></span><span></span><span></span><span></span></div>

  <!-- What we do -->
  <svg class="divider abs" style="top:655px" viewBox="0 0 1050 40"><line x1="0" y1="22" x2="1050" y2="22" stroke="#cfcfcf" stroke-width="1.5"/><path d="M495 6 Q540 8 566 30 Q540 16 495 6Z" fill="var(--brand)"/></svg>
  <h2 class="section-title abs" style="top:712px">What We Do?</h2>

  <div class="service is-active abs" style="left:59px;top:826px">
    <div class="service-icon is-active"><svg width="44" height="40" viewBox="0 0 44 40"><g fill="#0a2a55"><circle cx="14" cy="8" r="5"/><path d="M9 14h10l2 18H7z"/><rect x="5" y="32" width="18" height="6"/><circle cx="30" cy="12" r="4"/><path d="M26 17h8l2 15h-12z"/><rect x="22" y="32" width="16" height="6"/></g></svg></div>
    <h3>Strategy</h3>
    <p>Sed vel magna vel eros adipiscing adipiscing eu sit amet turpis. Mauris et massa sed lacus tempus pellentesque.</p>
  </div>
  <div class="service abs" style="left:328px;top:826px">
    <div class="service-icon"><svg width="44" height="40" viewBox="0 0 44 40"><g fill="#444"><circle cx="12" cy="9" r="4"/><circle cx="22" cy="7" r="5"/><circle cx="32" cy="9" r="4"/><path d="M6 16h12v18H6zM16 14h12v22H16zM26 16h12v18H26z"/></g></svg></div>
    <h3>People</h3>
    <p>Sed vel magna vel eros adipiscing adipiscing eu sit amet turpis. Mauris et massa sed lacus tempus pellentesque.</p>
  </div>
  <div class="service abs" style="left:599px;top:826px">
    <div class="service-icon"><svg width="40" height="40" viewBox="0 0 40 40"><g fill="none" stroke="#444" stroke-width="5"><path d="M8 18A12 12 0 0 1 30 12"/><path d="M32 22A12 12 0 0 1 10 28"/></g><path d="M26 6l8 2-2 8z" fill="#444"/><path d="M14 34l-8-2 2-8z" fill="#444"/></svg></div>
    <h3>Process</h3>
    <p>Sed vel magna vel eros adipiscing adipiscing eu sit amet turpis. Mauris et massa sed lacus tempus pellentesque.</p>
  </div>
  <div class="service abs" style="left:871px;top:826px">
    <div class="service-icon"><svg width="44" height="40" viewBox="0 0 44 40"><g fill="none" stroke="#444"><circle cx="16" cy="22" r="8" stroke-width="5" stroke-dasharray="4 2.3"/><circle cx="16" cy="22" r="3" stroke-width="2"/><circle cx="32" cy="11" r="6" stroke-width="4" stroke-dasharray="3 2"/><circle cx="32" cy="11" r="2" stroke-width="2"/></g></svg></div>
    <h3>Technology</h3>
    <p>Sed vel magna vel eros adipiscing adipiscing eu sit amet turpis. Mauris et massa sed lacus tempus pellentesque.</p>
  </div>

  <!-- Feature rows -->
  <div class="feature-photo abs" style="left:0;top:1141px;background:linear-gradient(180deg,#eef0f2,#c9ccd1 60%,#e4e6e8)" role="img" aria-label="Large group of business people in dark suits walking forward"></div>
  <section class="feature-panel abs" style="left:600px;top:1141px">
    <h2>Who We Are?</h2>
    <p>Nunc consequat congue nulla eu imperdiet. Donec in est erat, id malesuada turpis. Nunc a dui id turpis convallis semper. Nunc dignissim lectus vitae eros placerat euismod. Aenean lacinia sodales eros, sit amet molestie enim consectetur eget. Sed vel magna vel eros adipiscing adipiscing eu sit amet turpis.</p>
    <span class="btn btn-solid">Learn More</span>
  </section>

  <section class="feature-panel left abs" style="left:0;top:1545px">
    <h2>Who We Serve?</h2>
    <p>Nunc consequat congue nulla eu imperdiet. Donec in est erat, id malesuada turpis. Nunc a dui id turpis convallis semper. Nunc dignissim lectus vitae eros placerat euismod. Aenean lacinia sodales eros, sit amet molestie enim consectetur eget. Sed vel magna vel eros adipiscing adipiscing eu sit amet turpis.</p>
    <span class="btn btn-outline">Learn More</span>
  </section>
  <div class="feature-photo abs" style="left:600px;top:1545px;background:linear-gradient(135deg,#d7dde4,#8e98a6 55%,#eef1f4)" role="img" aria-label="Business partners shaking hands across a meeting table with a laptop"></div>

  <div class="feature-photo abs" style="left:0;top:1949px;background:linear-gradient(135deg,#f2f3f5,#b8bcc2 55%,#e2e4e7)" role="img" aria-label="Customer service agent with a headset working with colleagues in an office"></div>
  <section class="feature-panel abs" style="left:600px;top:1949px">
    <h2>Whom We Help?</h2>
    <p>Nunc consequat congue nulla eu imperdiet. Donec in est erat, id malesuada turpis. Nunc a dui id turpis convallis semper. Nunc dignissim lectus vitae eros placerat euismod. Aenean lacinia sodales eros, sit amet molestie enim consectetur eget. Sed vel magna vel eros adipiscing adipiscing eu sit amet turpis.</p>
    <span class="btn btn-outline">Learn More</span>
  </section>

  <!-- Testimonials -->
  <svg class="divider abs" style="top:2396px" viewBox="0 0 1050 40"><line x1="0" y1="22" x2="1050" y2="22" stroke="#cfcfcf" stroke-width="1.5"/><path d="M495 6 Q540 8 566 30 Q540 16 495 6Z" fill="var(--brand)"/></svg>
  <h2 class="section-title abs" style="top:2456px">Testimonials</h2>
  <p class="quote abs">Vestibulum vel metus sit amet turpis bibendum tincidunt vel sit amet quam. Pellentesque habitant morbi tristique senectus et netus et malesuada fames ac turpis egestas. Nunc consequat congue nulla eu imperdiet. Donec in est erat, id malesuada turpis. Nunc a dui id turpis convallis semper. Nunc dignissim lectus vitae eros placerat euismod. Aenean lacinia sodales eros, sit amet molestie enim consectetur eget.</p>
  <svg class="slider-arrow abs" style="left:74px" width="20" height="30" viewBox="0 0 20 30"><path d="M16 2L4 15L16 28" fill="none" stroke="#aaa" stroke-width="4"/></svg>
  <svg class="slider-arrow abs" style="left:1106px" width="20" height="30" viewBox="0 0 20 30"><path d="M4 2L16 15L4 28" fill="none" stroke="#aaa" stroke-width="4"/></svg>
  <div class="avatar abs" role="img" aria-label="Client portrait"></div>
  <div class="quote-mark abs">&ldquo;&rdquo;</div>

  <!-- Footer -->
  <footer class="site-footer abs"></footer>
  <h2 class="footer-title abs" style="left:78px;top:2858px">Let Us Talk</h2>
  <div class="field abs" style="left:75px;top:2945px;width:309px;height:44px">Name</div>
  <div class="field abs" style="left:396px;top:2945px;width:307px;height:44px">Email Address</div>
  <div class="field abs" style="left:75px;top:2999px;width:628px;height:150px">Message</div>
  <div class="send abs">Send Message</div>

  <h2 class="footer-title abs" style="left:764px;top:2858px">Contact Address</h2>
  <div class="contact-name abs">Shift Pathways</div>
  <div class="contact-addr abs">2218 Meridian Lane,<br>Harbor City CA 90210</div>
  <ul class="contact-list abs">
    <li><svg width="12" height="12" viewBox="0 0 12 12"><path d="M2 1l3 3-1.5 1.5a7 7 0 0 0 3 3L8 7l3 3-2 2C5 12 0 7 0 3z" fill="var(--azure)"/></svg>(555) 014-2207</li>
    <li><svg width="12" height="12" viewBox="0 0 12 12"><rect x="2" y="0" width="8" height="4" fill="#ccc"/><rect x="0" y="4" width="12" height="6" fill="#ccc"/><rect x="2" y="8" width="8" height="4" fill="#fff"/></svg>(555) 014-2207</li>
    <li><svg width="12" height="12" viewBox="0 0 12 12"><rect x="3" y="0" width="6" height="12" rx="1" fill="#ccc"/></svg>(555) 014-2207</li>
    <li><svg width="12" height="12" viewBox="0 0 12 12"><path d="M2 1l3 3-1.5 1.5a7 7 0 0 0 3 3L8 7l3 3-2 2C5 12 0 7 0 3z" fill="#ccc"/></svg>info@shiftpathways.example</li>
  </ul>

  <div class="bottom">
    <div class="brand"><span class="brand-mark"></span><span class="brand-name">Shift Pathways</span></div>
  </div>
  <p class="copyright abs">Copyright © 2015. All Right Reserved. Privacy Policy</p>

</div>
</body>
</html>
```